Corporate Two Sided Business Card

Looking for a Corporate "edgy" Modern look and feel for a business card

We are looking at two options. Dark background with our logo on it, white background with our logo on it - The background is more - Charcoal / Graphite then black

Details will be

Danielle Forsk

Licensee / Director

m. 0428 519 064

e. danielle@quorvela.com.au

quorvela.com.au

Target Market(s)

Professional Business people that refer use business and clients that own Investment Properties

Industry/Entity Type

Business

Contact Information for Business Card

Details will be

Danielle Forsk

Licensee / Director

m. 0428 519 064

quorvela.com.au

Font styles to use
Serif

Colors
000000
ec1f27
eeeeee
ffffff

Requirements
Must have
• Two options - White Background and Dark Background. - Two sided
Nice to have
• A design that is edgy, modern and new to look instead of boring style corporate cards - It should be a full integrated design
Should not have
• Block looking - Cheap.

```html
<!DOCTYPE html>
<html lang="en">
<head>
<meta charset="utf-8">
<title>Quorvela – Business Cards</title>
<link rel="stylesheet" href="https://fonts.googleapis.com/css2?family=Montserrat:wght@500;600&family=Arimo:wght@400;700&display=swap">
<style>
  :root {
    --stage: #1d1d1f;
    --graphite: #4a4a4d;
    --graphite-dark: #3c3c3f;
    --paper: #ffffff;
    --paper-shade: #eeeeee;
    --ink: #3a3a3c;
    --ink-soft: #5a5a5c;
    --red: #ec1f27;
    --blush: rgba(236, 31, 39, 0.22);
    --logo-light: #e6e6e6;
  }
  * { margin: 0; padding: 0; box-sizing: border-box; }
  html, body {
    width: 1200px;
    height: 997px;
    overflow: hidden;
    background: var(--stage);
  }
  .stage {
    width: 1200px;
    height: 997px;
    display: flex;
    flex-direction: column;
    align-items: center;
    justify-content: center;
    gap: 64px;
  }
  .card {
    width: 600px;
    height: 366px;
    border-radius: 20px;
    position: relative;
    overflow: hidden;
    box-shadow: 0 18px 40px rgba(0, 0, 0, 0.55);
  }
  .card--back {
    background: linear-gradient(160deg, var(--graphite) 0%, var(--graphite-dark) 100%);
    display: flex;
    align-items: center;
    justify-content: center;
  }
  .wordmark {
    display: flex;
    align-items: center;
    gap: 14px;
    font-family: "Montserrat", Arial, sans-serif;
    font-weight: 600;
    letter-spacing: -0.5px;
    line-height: 1;
  }
  .wordmark__mark {
    width: 34px;
    height: 34px;
    background: var(--red);
    flex: none;
  }
  .card--back .wordmark { font-size: 74px; color: var(--logo-light); }
  .card--back .wordmark__mark { width: 44px; height: 44px; }

  .card--front {
    background: linear-gradient(135deg, var(--paper) 0%, var(--paper) 55%, var(--paper-shade) 100%);
  }
  .card__accent {
    position: absolute;
    right: -40px;
    top: -20px;
    width: 300px;
    height: 420px;
    background: linear-gradient(200deg, var(--blush) 0%, rgba(236, 31, 39, 0.08) 100%);
  }
  .card--front .wordmark {
    position: absolute;
    left: 48px;
    top: 62px;
    font-size: 64px;
    color: var(--ink);
  }
  .card--front .wordmark__mark { width: 40px; height: 40px; }

  .identity {
    position: absolute;
    left: 48px;
    top: 190px;
    padding-left: 16px;
    border-left: 6px solid var(--ink-soft);
    font-family: "Arimo", Arial, sans-serif;
  }
  .identity__name {
    font-weight: 700;
    font-size: 19px;
    color: var(--ink);
    text-transform: uppercase;
    letter-spacing: 0.3px;
  }
  .identity__role {
    font-size: 15px;
    color: var(--red);
    margin-top: 3px;
  }
  .contact {
    position: absolute;
    left: 48px;
    top: 262px;
    list-style: none;
    font-family: "Arimo", Arial, sans-serif;
    font-size: 15px;
    color: var(--ink-soft);
  }
  .contact li {
    display: flex;
    align-items: center;
    gap: 10px;
    height: 24px;
  }
  .contact__icon { width: 18px; height: 18px; flex: none; }
  .contact__spacer { width: 18px; flex: none; }
  .contact__web {
    font-weight: 700;
    color: var(--red);
    letter-spacing: 0.4px;
    text-transform: uppercase;
  }
</style>
</head>
<body>
<main class="stage">
  <section class="card card--back" aria-label="Card back, graphite">
    <div class="wordmark">
      <span class="wordmark__mark"></span>
      <span class="wordmark__name">quorvela</span>
    </div>
  </section>

  <section class="card card--front" aria-label="Card front, white">
    <div class="card__accent" role="img" aria-label="Faint red brand decoration"></div>
    <div class="wordmark">
      <span class="wordmark__mark"></span>
      <span class="wordmark__name">quorvela</span>
    </div>
    <div class="identity">
      <p class="identity__name">Danielle Forsk</p>
      <p class="identity__role">Licensee / Director</p>
    </div>
    <ul class="contact">
      <li>
        <svg class="contact__icon" viewBox="0 0 18 18" aria-hidden="true">
          <circle cx="9" cy="9" r="9" fill="#ec1f27"/>
          <path d="M6 5.2c.5-.4 1-.3 1.3.2l.7 1.3c.2.4.1.8-.2 1l-.5.4c.4.9 1 1.5 1.9 1.9l.4-.5c.3-.3.7-.4 1-.2l1.3.7c.5.3.6.8.2 1.3l-.6.7c-.5.5-1.3.6-2 .3-2-.9-3.5-2.4-4.4-4.4-.3-.7-.2-1.5.3-2z" fill="#fff"/>
        </svg>
        <span>0428 519 064</span>
      </li>
      <li>
        <svg class="contact__icon" viewBox="0 0 18 18" aria-hidden="true">
          <circle cx="9" cy="9" r="9" fill="#ec1f27"/>
          <rect x="4.5" y="6" width="9" height="6.5" rx="0.8" fill="none" stroke="#fff" stroke-width="1.2"/>
          <path d="M4.8 6.4 9 9.6l4.2-3.2" fill="none" stroke="#fff" stroke-width="1.2"/>
        </svg>
        <span>e.danielle@quorvela.com.au</span>
      </li>
      <li>
        <span class="contact__spacer"></span>
        <span class="contact__web">www.quorvela.com.au</span>
      </li>
    </ul>
  </section>
</main>
</body>
</html>
```